Unique, Impressive, and Modern Business Card

Looking for a distinctive, unique business card. We are distributors of tire repairs supplies, tools, machinery, and chemicals. Our target market are tire repair shops, tire franchises, and mechanic shops. We would like our design to include tire characteristics, and use our business colors. Feel free to use all types design and printing options (emboss, spot uv, foil, etc) QR code may be applied, you can use different size business cards ( standard, square, rounded edge, colored edge, etc), all formats needed for printing, also editable for future changes

Target Market(s)

Automotive, Tire industries

Industry/Entity Type

Tire Industry (automotive)

Contact Information for Business Card

Business logo, business Name (Quillmark Industries Inc), Name (Dorian Pelham), Position (President) Address (41 Fernhollow Lane, Marston NY 10293), Contact number (Company 1-855-302-4418, Cell 1-516-248-3907, email address (dorian.pelham@quillmarkusa.example), URL (www.quillmarkusa.example

Requirements
Must have
• Must include Business Colors (Black, Green, Blue, White) see sample website file
Nice to have
• emboss, spot uv, etc

```html
<!DOCTYPE html>
<html lang="en">
<head>
<meta charset="utf-8">
<title>Quillmark Industries – Business Card</title>
<link href="https://fonts.googleapis.com/css2?family=Arimo:wght@400;700&display=swap" rel="stylesheet">
<style>
  :root {
    --brand-blue: #0019e0;
    --ink: #111111;
    --paper: #ffffff;
    --stage: #d9d9d9;
    --faint: #ececec;
    --faint-dot: #e6e8fb;
    --gear-light: #c9c9c9;
    --gear-dark: #3a3a3a;
  }
  * { margin: 0; padding: 0; box-sizing: border-box; }
  html, body { width: 1200px; height: 900px; overflow: hidden; }
  body {
    background: var(--stage);
    font-family: "Arimo", Arial, sans-serif;
    position: relative;
  }
  .card {
    position: absolute;
    width: 640px;
    height: 366px;
    border-radius: 26px;
    overflow: hidden;
    box-shadow: 0 6px 14px rgba(0,0,0,0.25);
  }
  /* Front */
  .card--front { left: 80px; top: 60px; background: var(--brand-blue); }
  .gear-photo {
    position: absolute;
    left: 355px; top: 40px;
    width: 200px; height: 150px;
    border-radius: 50% / 45%;
    background: radial-gradient(ellipse at 45% 40%, var(--gear-light), #8a8a8a 55%, var(--gear-dark));
  }
  .brand {
    position: absolute;
    display: flex;
    align-items: center;
    gap: 14px;
  }
  .brand__dot { width: 46px; height: 46px; border-radius: 50%; }
  .brand__name { font-weight: 700; letter-spacing: 1px; line-height: 1; }
  .card--front .brand { left: 48px; bottom: 56px; }
  .card--front .brand__dot { background: var(--paper); }
  .card--front .brand__name { color: var(--paper); font-size: 34px; }

  /* Back */
  .card--back { left: 480px; top: 474px; background: var(--paper); }
  .faint-ring {
    position: absolute;
    right: -40px; top: -30px;
    width: 330px; height: 330px;
    border-radius: 50%;
    background: var(--faint);
  }
  .faint-ring::after {
    content: "";
    position: absolute;
    left: 110px; top: 110px;
    width: 110px; height: 110px;
    border-radius: 50%;
    background: var(--faint-dot);
  }
  .card--back .brand { left: 40px; top: 44px; }
  .card--back .brand__dot { background: var(--ink); width: 58px; height: 58px; }
  .card--back .brand__name { color: var(--ink); font-size: 38px; }
  .person { position: absolute; left: 42px; top: 152px; }
  .person__name { font-size: 30px; color: var(--ink); letter-spacing: 0.5px; }
  .person__title { font-size: 22px; color: var(--brand-blue); margin-top: 2px; }
  .contacts { position: absolute; left: 42px; top: 232px; list-style: none; }
  .contacts li {
    display: flex; align-items: center; gap: 10px;
    font-size: 19px; color: var(--ink); height: 26px;
  }
  .contacts svg { width: 18px; height: 18px; fill: var(--brand-blue); flex: none; }
  .address {
    position: absolute; right: 34px; top: 140px;
    text-align: right; font-size: 19px; line-height: 1.35; color: var(--ink);
  }
  .address__company { color: var(--brand-blue); }
</style>
</head>
<body>

<section class="card card--front">
  <div class="gear-photo" role="img" aria-label="Photograph of a steel transmission gear shaft"></div>
  <div class="brand">
    <span class="brand__dot"></span>
    <span class="brand__name">QUILLMARK INDUSTRIES</span>
  </div>
</section>

<section class="card card--back">
  <div class="faint-ring" aria-hidden="true"></div>
  <div class="brand">
    <span class="brand__dot"></span>
    <span class="brand__name">QUILLMARK INDUSTRIES</span>
  </div>

  <div class="person">
    <p class="person__name">DORIAN PELHAM</p>
    <p class="person__title">President</p>
  </div>

  <ul class="contacts">
    <li>
      <svg viewBox="0 0 24 24" aria-hidden="true"><path d="M6.6 10.8a15 15 0 0 0 6.6 6.6l2.2-2.2c.3-.3.7-.4 1-.2 1.1.4 2.3.6 3.6.6.6 0 1 .4 1 1V20c0 .6-.4 1-1 1A17 17 0 0 1 3 4c0-.6.4-1 1-1h3.5c.6 0 1 .4 1 1 0 1.3.2 2.5.6 3.6.1.3 0 .7-.2 1z"/></svg>
      1-855-302-4418
    </li>
    <li>
      <svg viewBox="0 0 24 24" aria-hidden="true"><path d="M7 1h10a2 2 0 0 1 2 2v18a2 2 0 0 1-2 2H7a2 2 0 0 1-2-2V3a2 2 0 0 1 2-2zm0 3v14h10V4zm5 15.5a1.2 1.2 0 1 0 0 2.4 1.2 1.2 0 0 0 0-2.4z"/></svg>
      1-516-248-3907
    </li>
    <li>
      <svg viewBox="0 0 24 24" aria-hidden="true"><path d="M2 5h20v14H2zm2 2v.5l8 5 8-5V7zm0 2.8V17h16V9.8l-8 5z"/></svg>
      dorian.pelham@quillmarkusa.example
    </li>
    <li>
      <svg viewBox="0 0 24 24" aria-hidden="true"><path d="M12 2a10 10 0 1 0 0 20 10 10 0 0 0 0-20zm6.9 6h-2.9a15 15 0 0 0-1.4-3.6A8 8 0 0 1 18.9 8zM12 4c.8 1.2 1.5 2.5 1.9 4h-3.8c.4-1.5 1.1-2.8 1.9-4zM4.3 14a8 8 0 0 1 0-4h3.4a16 16 0 0 0 0 4zm.8 2h2.9c.3 1.3.8 2.5 1.4 3.6A8 8 0 0 1 5.1 16zM8 8H5.1a8 8 0 0 1 4.3-3.6C8.8 5.5 8.3 6.7 8 8zm4 12c-.8-1.2-1.5-2.5-1.9-4h3.8c-.4 1.5-1.1 2.8-1.9 4zm2.3-6H9.7a14 14 0 0 1 0-4h4.6a14 14 0 0 1 0 4zm.3 5.6c.6-1.1 1.1-2.3 1.4-3.6h2.9a8 8 0 0 1-4.3 3.6zm1.7-5.6a16 16 0 0 0 0-4h3.4a8 8 0 0 1 0 4z"/></svg>
      www.quillmarkusa.example
    </li>
  </ul>

  <address class="address">
    <span class="address__company">Quillmark Industries Inc</span><br>
    41 Fernhollow Lane<br>
    Marston NY 10293
  </address>
</section>

</body>
</html>
```